Need simple and modern looking business card with all my information on one side and logo on the other side
Info :
Company name - VELMAR CONSTRUCTION LLC
Company addres- 418 harbor 87th. Dunmoor park ny 10352
Email- velmarllc@tridomail.Com
Company phone number 555-318-6094
Cell number- 555-742-0583
Web site - velmarllc.Com
My name Gerald tomasino

Target Market(s)

Construction , home improvement, remodeling

Industry/Entity Type

Construction

Contact Information for Business Card

It has to be moder but at the same time simple

Font styles to use
Sans Serif

Colors
0255a3
ffffff
000000
f78f20
b1b1b1
9d9d9d
1b1b1b
33a6d7
ec1f27

Requirements
Must have
• My logo on one side maybe with a some kind of background on the other side all my information
Nice to have
• Some kind of background pictures provided by you .PLEASE HAVE ACCOUNT WITH PIXELVAULT WILL NOT PAY ANY EXTRA FEES .
Should not have
• Any kind of hamer, nails,screws, helmets itp. Please do not copy the other designs come up with something new.

```html
<!DOCTYPE html>
<html lang="en">
<head>
<meta charset="utf-8">
<title>Velmar Construction LLC – Business Card</title>
<link rel="stylesheet" href="https://fonts.googleapis.com/css2?family=Open+Sans:wght@400;600;700&display=swap">
<style>
  :root {
    --page-bg: #d9d9db;
    --card-front: #efefed;
    --card-back-top: #e6ebef;
    --card-back-bottom: #d3dde4;
    --orange: #f78f20;
    --red: #ec1f27;
    --ink: #1b1b1b;
    --blue: #0255a3;
    --grey: #9d9d9d;
  }
  * { box-sizing: border-box; margin: 0; padding: 0; }
  html, body { width: 1200px; height: 900px; overflow: hidden; }
  body {
    background: var(--page-bg);
    font-family: "Open Sans", Arial, sans-serif;
    position: relative;
  }
  .card {
    position: absolute;
    left: 290px;
    width: 620px;
    height: 354px;
    overflow: hidden;
    box-shadow: 0 6px 18px rgba(0,0,0,0.18);
  }
  .card--front { top: 76px; background: var(--card-front); }
  .card--back  { top: 470px; }

  .card__band {
    position: absolute;
    left: 0; right: 0; bottom: 0;
    height: 22px;
    display: flex;
  }
  .card__band-orange { flex: 0 0 56%; background: var(--orange); }
  .card__band-red { flex: 1; background: var(--red); }

  .brand {
    display: flex;
    align-items: center;
    gap: 10px;
  }
  .brand__mark {
    width: 16px; height: 16px;
    background: var(--orange);
    flex: none;
  }
  .brand__name {
    font-weight: 700;
    color: var(--ink);
    letter-spacing: 0.04em;
    line-height: 1;
    white-space: nowrap;
  }

  .card--front .brand {
    position: absolute;
    top: 140px;
    left: 0; right: 0;
    justify-content: center;
  }
  .card--front .brand__name { font-size: 27px; }
  .front__web {
    position: absolute;
    top: 218px;
    left: 0; right: 0;
    text-align: center;
    color: var(--orange);
    font-size: 13px;
    letter-spacing: 0.32em;
  }

  .back__scene {
    position: absolute;
    inset: 0;
    background:
      linear-gradient(100deg, rgba(255,255,255,0.55) 0%, rgba(255,255,255,0) 55%),
      linear-gradient(180deg, var(--card-back-top) 0%, var(--card-back-bottom) 100%);
  }
  .card--back .brand {
    position: absolute;
    top: 108px;
    left: 34px;
  }
  .card--back .brand__name { font-size: 21px; }
  .back__person {
    position: absolute;
    left: 34px;
    top: 218px;
    color: var(--orange);
    font-weight: 700;
    font-size: 17px;
  }
  .back__web {
    position: absolute;
    left: 34px;
    top: 290px;
    color: var(--orange);
    font-size: 14px;
  }
  .contact {
    position: absolute;
    left: 380px;
    top: 62px;
    list-style: none;
    color: var(--orange);
    font-size: 12.5px;
  }
  .contact__item {
    display: flex;
    align-items: center;
    gap: 10px;
    height: 24px;
  }
  .contact__icon { width: 13px; height: 13px; flex: none; }
  .contact__address {
    position: absolute;
    left: 402px;
    top: 160px;
    color: var(--orange);
    font-size: 12.5px;
    line-height: 1.45;
    font-style: normal;
  }
</style>
</head>
<body>

<section class="card card--front" aria-label="Business card front">
  <div class="brand">
    <span class="brand__mark"></span>
    <span class="brand__name">VELMAR CONSTRUCTION LLC</span>
  </div>
  <p class="front__web">www.velmarllc.com</p>
  <div class="card__band"><span class="card__band-orange"></span><span class="card__band-red"></span></div>
</section>

<section class="card card--back" aria-label="Business card back">
  <div class="back__scene" role="img" aria-label="Faint pale-blue city skyline photograph behind the contact details"></div>

  <div class="brand">
    <span class="brand__mark"></span>
    <span class="brand__name">VELMAR CONSTRUCTION LLC</span>
  </div>

  <p class="back__person">Gerald Tomasino</p>
  <p class="back__web">www.velmarllc.com</p>

  <ul class="contact">
    <li class="contact__item">
      <svg class="contact__icon" viewBox="0 0 16 16" aria-hidden="true">
        <circle cx="8" cy="8" r="7" fill="none" stroke="#ec1f27" stroke-width="1.4"/>
        <path d="M5.5 4.5l1.5 1.5-1 1c.6 1.2 1.3 1.9 2.5 2.5l1-1 1.5 1.5-1 1c-2.5-.5-4.5-2.5-5-5z" fill="#ec1f27"/>
      </svg>
      <span>555-318-6094</span>
    </li>
    <li class="contact__item">
      <svg class="contact__icon" viewBox="0 0 16 16" aria-hidden="true">
        <rect x="4" y="1.5" width="8" height="13" rx="1.5" fill="none" stroke="#ec1f27" stroke-width="1.4"/>
        <circle cx="8" cy="12" r="0.9" fill="#ec1f27"/>
      </svg>
      <span>555-742-0583</span>
    </li>
    <li class="contact__item">
      <svg class="contact__icon" viewBox="0 0 16 16" aria-hidden="true">
        <rect x="1.5" y="3.5" width="13" height="9" fill="none" stroke="#ec1f27" stroke-width="1.4"/>
        <path d="M1.5 3.5L8 9l6.5-5.5" fill="none" stroke="#ec1f27" stroke-width="1.4"/>
      </svg>
      <span>velmarllc@tridomail.Com</span>
    </li>
  </ul>

  <address class="contact__address">418 harbor 87th. Dunmoor<br>Park ny 10352</address>

  <div class="card__band"><span class="card__band-orange"></span><span class="card__band-red"></span></div>
</section>

</body>
</html>
```